Simple graphic for a book or slide presentation

We are looking for a style that suits the style of our book. It's title is Harbor. Keeping a calm course through stormy seas. There will be more line drawing/graphics in the book but how you design this image will create the style for all the other simple graphics in the book (once we decide what they are). So this one design will lead to a few more to match the style of this one. We'd like the shape of the overall graphic (i.e the arrows and words/bubbles) to be circular (not a rounded square as appears in the sample attached). Perhaps the words don't need to be in ovals or bound by anything at all; perhaps they do - let's see what you see. We'd like you to choose a font or offer many different fonts you think will capture the practical yet unconventional tone of the book. The book is teaching that managing risks in life is a life-skill that can be learned. The section of the book where this graphic will be placed is called "the power of language" - basically we are saying that thoughts, words and actions create our culture and our destiny. This insight comes from Torvel Pelloru's famous quote:
Carefully watch your thoughts, for they become your words.
Manage and watch your words, for they will become your actions.
Consider and judge your actions, for they have become your habits.
Acknowledge and watch your habits, for they shall become your values.
Understand and embrace your values, for they become your destiny.

Please change the text in the middle of the graphic to say: The Human Culture Cycle

```html
<!DOCTYPE html>
<html lang="en">
<head>
<meta charset="utf-8">
<title>The Human Culture Cycle</title>
<link rel="stylesheet" href="https://fonts.googleapis.com/css2?family=Montserrat:wght@500;700&display=swap">
<style>
  :root {
    --page-bg: #ffffff;
    --ring-light: #dcdddf;
    --ring-dark: #a9abae;
    --face-light: #fbfbfb;
    --face-dark: #eeeeef;
    --hub-halo: #e4e5e7;
    --arrow: #c9cacc;
    --icon-tone: #96979b;
    --icon-tone-soft: #c4c5c8;
    --label: #3a3b3d;
  }
  html, body {
    margin: 0;
    padding: 0;
    width: 1200px;
    height: 1200px;
    overflow: hidden;
    background: var(--page-bg);
  }
  .cycle-diagram {
    display: block;
    width: 1200px;
    height: 1200px;
  }
  .node-label {
    font-family: "Montserrat", sans-serif;
    font-weight: 700;
    font-size: 30px;
    fill: var(--label);
    text-anchor: middle;
    letter-spacing: 0.5px;
  }
  .hub-title {
    font-family: "Montserrat", sans-serif;
    font-weight: 500;
    font-size: 45px;
    fill: var(--label);
    text-anchor: middle;
    letter-spacing: 1px;
  }
  .cycle-arrow {
    fill: none;
    stroke: var(--arrow);
    stroke-width: 6;
  }
</style>
</head>
<body>
<svg class="cycle-diagram" viewBox="0 0 1200 1200" xmlns="http://www.w3.org/2000/svg" aria-labelledby="diagram-title">
  <title id="diagram-title">The Human Culture Cycle: Thoughts, Words, Actions, Habits, Values, Culture</title>
  <defs>
    <linearGradient id="ring-gradient" x1="0" y1="0" x2="1" y2="1">
      <stop offset="0" stop-color="var(--ring-light)"/>
      <stop offset="1" stop-color="var(--ring-dark)"/>
    </linearGradient>
    <linearGradient id="face-gradient" x1="0" y1="0" x2="1" y2="1">
      <stop offset="0" stop-color="var(--face-dark)"/>
      <stop offset="1" stop-color="var(--face-light)"/>
    </linearGradient>
    <radialGradient id="icon-gradient" cx="0.4" cy="0.4" r="0.7">
      <stop offset="0" stop-color="var(--icon-tone-soft)"/>
      <stop offset="1" stop-color="var(--icon-tone)"/>
    </radialGradient>
    <filter id="hub-shadow" x="-20%" y="-20%" width="140%" height="140%">
      <feDropShadow dx="8" dy="10" stdDeviation="8" flood-color="#9a9b9e" flood-opacity="0.45"/>
    </filter>
    <marker id="arrow-head" viewBox="0 0 10 10" refX="2" refY="5" markerWidth="24" markerHeight="24" markerUnits="userSpaceOnUse" orient="auto">
      <path d="M0 0 L10 5 L0 10 L2.5 5 Z" fill="var(--arrow)"/>
    </marker>
  </defs>

  <!-- connecting arrows -->
  <g class="cycle-arrows">
    <path class="cycle-arrow" d="M745.3 215.8 A413 413 0 0 1 858.3 278.6" marker-end="url(#arrow-head)"/>
    <path class="cycle-arrow" d="M1010.7 532.3 A413 413 0 0 1 1013.0 661.5" marker-end="url(#arrow-head)"/>
    <path class="cycle-arrow" d="M869.5 920.4 A413 413 0 0 1 758.7 986.9" marker-end="url(#arrow-head)"/>
    <path class="cycle-arrow" d="M462.7 992.1 A413 413 0 0 1 349.7 929.4" marker-end="url(#arrow-head)"/>
    <path class="cycle-arrow" d="M197.3 675.7 A413 413 0 0 1 195.0 546.5" marker-end="url(#arrow-head)"/>
    <path class="cycle-arrow" d="M338.5 287.6 A413 413 0 0 1 449.3 221.1" marker-end="url(#arrow-head)"/>
  </g>

  <!-- central hub -->
  <g class="hub">
    <circle cx="604" cy="604" r="203" fill="var(--hub-halo)"/>
    <circle cx="604" cy="604" r="175" fill="url(#face-gradient)" filter="url(#hub-shadow)"/>
    <text class="hub-title">
      <tspan x="604" y="535">The</tspan>
      <tspan x="604" y="591">Human</tspan>
      <tspan x="604" y="646">Culture</tspan>
      <tspan x="604" y="702">Cycle</tspan>
    </text>
  </g>

  <!-- stage nodes -->
  <g class="stage stage-thoughts" transform="translate(604 191)">
    <circle r="129" fill="url(#ring-gradient)"/>
    <circle r="114" fill="url(#face-gradient)"/>
    <rect x="-55" y="-95" width="110" height="88" rx="30" fill="url(#icon-gradient)" role="img" aria-label="Icon: head in profile with a thought cloud"/>
    <text class="node-label" y="67">Thoughts</text>
  </g>

  <g class="stage stage-words" transform="translate(961 397)">
    <circle r="129" fill="url(#ring-gradient)"/>
    <circle r="114" fill="url(#face-gradient)"/>
    <rect x="-55" y="-88" width="110" height="100" rx="30" fill="url(#icon-gradient)" role="img" aria-label="Icon: speaking head with sound waves"/>
    <text class="node-label" y="57">Words</text>
  </g>

  <g class="stage stage-actions" transform="translate(961 810)">
    <circle r="129" fill="url(#ring-gradient)"/>
    <circle r="114" fill="url(#face-gradient)"/>
    <rect x="-55" y="-75" width="110" height="95" rx="30" fill="url(#icon-gradient)" role="img" aria-label="Icon: hand gripping a hammer"/>
    <text class="node-label" y="60">Actions</text>
  </g>

  <g class="stage stage-habits" transform="translate(604 1016)">
    <circle r="129" fill="url(#ring-gradient)"/>
    <circle r="114" fill="url(#face-gradient)"/>
    <rect x="-50" y="-82" width="100" height="100" rx="30" fill="url(#icon-gradient)" role="img" aria-label="Icon: head in profile with gears inside"/>
    <text class="node-label" y="63">Habits</text>
  </g>

  <g class="stage stage-values" transform="translate(247 810)">
    <circle r="129" fill="url(#ring-gradient)"/>
    <circle r="114" fill="url(#face-gradient)"/>
    <rect x="-55" y="-70" width="110" height="97" rx="30" fill="url(#icon-gradient)" role="img" aria-label="Icon: two open hands holding a heart"/>
    <text class="node-label" y="66">Values</text>
  </g>

  <g class="stage stage-culture" transform="translate(247 397)">
    <circle r="129" fill="url(#ring-gradient)"/>
    <circle r="114" fill="url(#face-gradient)"/>
    <rect x="-62" y="-60" width="124" height="75" rx="30" fill="url(#icon-gradient)" role="img" aria-label="Icon: globe between two people"/>
    <text class="node-label" y="53">Culture</text>
  </g>
</svg>
</body>
</html>
```